Medical Practice Business Card

we need a business card for our new medical ophthalmology practice based in Needham Massachusetts. we are looking for a simple , modern and elegant design.
the card needs to contain the following
1- the logo of our practice (please see attached file)
2- the name of the practice : "Harbor Crest Vision Care"
3- Doctor's Name: Tobias Werrin MD PhD
4- Specialty: Board-Certified Vitreoretinal Surgeon
5- practice address: 382 Palden Ave, Suite 210, Larkfield VT 05491
7- Office number: 617- 418 - 2297
8- fax number: 617- 729 - 3186
9- email: info@hcvisioncare.com
10- website: www.hcvisioncare.com
see description

```html
<!DOCTYPE html>
<html lang="en">
<head>
<meta charset="utf-8">
<title>Harbor Crest Vision Care – Business Card</title>
<link href="https://fonts.googleapis.com/css2?family=Cinzel:wght@600&family=Tinos&display=swap" rel="stylesheet">
<style>
  :root {
    --stage: #232323;
    --teal: #1f9a9a;
    --blue: #0e55a7;
    --navy: #173a6b;
    --ink: #1b1b1b;
    --paper: #ffffff;
  }
  html, body {
    margin: 0;
    width: 1200px;
    height: 780px;
    overflow: hidden;
    background: var(--stage);
  }
  .canvas {
    position: relative;
    width: 1200px;
    height: 780px;
  }
  .card {
    position: absolute;
    top: 235px;
    width: 540px;
    height: 310px;
    overflow: hidden;
    box-shadow: 0 14px 30px rgba(0,0,0,.55);
  }
  .card--front {
    left: 40px;
    background: linear-gradient(160deg, var(--teal) 0%, #13789f 35%, var(--blue) 70%);
    display: flex;
    align-items: center;
    justify-content: center;
  }
  .card--back {
    left: 620px;
    background: var(--paper);
  }
  .brand {
    display: flex;
    align-items: center;
    gap: 12px;
    font-family: "Cinzel", serif;
    font-weight: 600;
    letter-spacing: .5px;
    white-space: nowrap;
  }
  .brand__dot {
    width: 14px;
    height: 14px;
    border-radius: 50%;
    flex: none;
  }
  .card--front .brand { color: var(--paper); font-size: 30px; }
  .card--front .brand__dot { background: var(--paper); }
  .card--back .brand {
    position: absolute;
    left: 28px;
    top: 34px;
    color: var(--navy);
    font-size: 19px;
  }
  .card--back .brand__dot { background: #6cc3de; width: 10px; height: 10px; }
  .doctor {
    position: absolute;
    right: 34px;
    top: 90px;
    text-align: right;
  }
  .doctor__name {
    font-family: "Cinzel", serif;
    font-weight: 600;
    font-size: 19px;
    color: var(--blue);
    margin: 0;
    white-space: nowrap;
  }
  .doctor__specialty {
    font-family: "Tinos", serif;
    font-size: 13px;
    color: var(--ink);
    margin: 4px 0 0;
    white-space: nowrap;
  }
  .tab {
    position: absolute;
    right: 0;
    top: 88px;
    width: 14px;
    height: 34px;
    background: linear-gradient(90deg, #6aa0e0, var(--blue));
  }
  .address {
    position: absolute;
    right: 34px;
    top: 144px;
    text-align: right;
    font-family: "Tinos", serif;
    font-size: 13px;
    line-height: 1.35;
    color: var(--ink);
    margin: 0;
    font-style: normal;
    white-space: nowrap;
  }
  .contacts {
    position: absolute;
    left: 28px;
    bottom: 30px;
    margin: 0;
    padding: 0;
    list-style: none;
    font-family: "Tinos", serif;
    font-size: 13px;
    color: var(--ink);
  }
  .contacts li {
    display: flex;
    align-items: center;
    gap: 8px;
    line-height: 20px;
    white-space: nowrap;
  }
  .contacts svg { width: 13px; height: 13px; fill: var(--blue); flex: none; }
  .swoosh {
    position: absolute;
    left: 0;
    top: 0;
    width: 540px;
    height: 310px;
  }
</style>
</head>
<body>
<main class="canvas">

  <section class="card card--front" aria-label="Card front">
    <div class="brand"><span class="brand__dot"></span>Harbor Crest Vision Care</div>
  </section>

  <section class="card card--back" aria-label="Card back">
    <svg class="swoosh" viewBox="0 0 540 310" aria-hidden="true">
      <defs>
        <linearGradient id="swooshFill" x1="0" y1="1" x2="1" y2="0">
          <stop offset="0" stop-color="#0e55a7"/>
          <stop offset=".6" stop-color="#1f8f9e"/>
          <stop offset="1" stop-color="#0e55a7"/>
        </linearGradient>
      </defs>
      <path d="M190 310 C310 262 420 228 540 212 L540 310 Z" fill="url(#swooshFill)"/>
      <path d="M320 310 C395 272 460 248 540 232" stroke="#fff" stroke-width="3" fill="none"/>
    </svg>

    <div class="brand"><span class="brand__dot"></span>Harbor Crest Vision Care</div>

    <span class="tab"></span>
    <div class="doctor">
      <p class="doctor__name">Tobias Werrin MD PhD</p>
      <p class="doctor__specialty">Board-Certified Vitreoretinal Surgeon</p>
    </div>

    <address class="address">382 Palden Ave, Suite 210,<br>Larkfield VT 05491</address>

    <ul class="contacts">
      <li><svg viewBox="0 0 16 16"><path d="M3 1l3 3-2 2c1 2 3 4 5 5l2-2 3 3-2 3C7 14 2 9 1 3z"/></svg>617- 418 - 2297</li>
      <li><svg viewBox="0 0 16 16"><rect x="1" y="6" width="14" height="9" rx="1"/><rect x="4" y="1" width="8" height="4"/></svg>617- 729 - 3186</li>
      <li><svg viewBox="0 0 16 16"><path d="M1 4h14v9H1z M1 4l7 5 7-5"/></svg>info@hcvisioncare.com</li>
      <li><svg viewBox="0 0 16 16"><circle cx="8" cy="8" r="7"/></svg>www.hcvisioncare.com</li>
    </ul>
  </section>

</main>
</body>
</html>
```